M&A Advisory firm needs elegant and powerful letterhead

We need a powerful but elegant letterhead to engage with the international financial industry.

Target Market(s)

New York and International Financial Industry

Industry/Entity Type

Finance

Font styles to use
Other font styles liked:
• Poppins

Requirements
Must have
• 482 W 17th Avenue 9th Floor New York, NY 10384 O: +1 (555) 804 2176 F: +1 (555) 804 2193

```html
<!DOCTYPE html>
<html lang="en">
<head>
<meta charset="utf-8">
<title>Meridane Letterhead</title>
<link href="https://fonts.googleapis.com/css2?family=Montserrat:wght@400;500;700&display=swap" rel="stylesheet">
<style>
  :root {
    --brand-blue: #15569a;
    --ink: #1d1d1f;
    --muted: #3a3a3c;
    --paper: #ffffff;
    --backdrop: #e9e9eb;
    --signature-tone: #d9dadd;
  }
  * { margin: 0; padding: 0; box-sizing: border-box; }
  html, body {
    width: 1146px;
    height: 1200px;
    overflow: hidden;
    background: var(--backdrop);
    font-family: "Montserrat", sans-serif;
    color: var(--ink);
  }
  .letterhead {
    position: absolute;
    left: 133px;
    top: 30px;
    width: 880px;
    height: 1140px;
    background: var(--paper);
    box-shadow: 0 6px 24px rgba(0,0,0,0.12);
  }
  .brand {
    position: absolute;
    left: 60px;
    top: 96px;
    display: flex;
    align-items: center;
    gap: 14px;
  }
  .brand-dot {
    width: 34px;
    height: 34px;
    border-radius: 50%;
    background: var(--brand-blue);
  }
  .brand-name {
    font-size: 50px;
    font-weight: 500;
    letter-spacing: 2px;
    color: var(--brand-blue);
  }
  .contact {
    position: absolute;
    right: 60px;
    top: 44px;
    text-align: right;
    font-size: 13px;
    line-height: 18px;
    color: var(--muted);
  }
  .contact-line {
    display: flex;
    justify-content: flex-end;
    align-items: center;
    gap: 6px;
  }
  .contact-icon { width: 12px; height: 12px; fill: var(--brand-blue); }
  .header-rule {
    position: absolute;
    left: 60px;
    right: 60px;
    top: 172px;
    height: 2px;
    background: var(--brand-blue);
  }
  .letter-body {
    position: absolute;
    left: 100px;
    top: 250px;
    width: 660px;
    font-size: 14.5px;
    line-height: 19px;
    color: var(--ink);
  }
  .salutation {
    font-weight: 700;
    font-size: 17px;
    margin-bottom: 12px;
  }
  .letter-body p.paragraph { margin-bottom: 30px; }
  .closing {
    margin-top: 34px;
    font-size: 14.5px;
  }
  .signature {
    margin-top: 12px;
    width: 200px;
    height: 80px;
    background: var(--signature-tone);
    border-radius: 4px;
  }
  .footer-band {
    position: absolute;
    left: 0;
    right: 0;
    bottom: 0;
    height: 30px;
    background: var(--brand-blue);
  }
</style>
</head>
<body>
  <main class="letterhead">
    <header>
      <div class="brand">
        <span class="brand-dot"></span>
        <span class="brand-name">MERIDANE</span>
      </div>
      <address class="contact">
        <div class="contact-line">
          <span>+1 (555) 804 2176</span>
          <svg class="contact-icon" viewBox="0 0 24 24" aria-hidden="true"><path d="M6.6 10.8a15.1 15.1 0 0 0 6.6 6.6l2.2-2.2c.3-.3.7-.4 1-.2 1.1.4 2.3.6 3.6.6.6 0 1 .4 1 1V20c0 .6-.4 1-1 1A17 17 0 0 1 3 4c0-.6.4-1 1-1h3.5c.6 0 1 .4 1 1 0 1.3.2 2.5.6 3.6.1.3 0 .7-.2 1z"/></svg>
        </div>
        <div class="contact-line">
          <span>+1 (555) 804 2193</span>
          <svg class="contact-icon" viewBox="0 0 24 24" aria-hidden="true"><path d="M7 3h9l3 3v4H7z M4 10h16a1 1 0 0 1 1 1v9a1 1 0 0 1-1 1H4a1 1 0 0 1-1-1v-9a1 1 0 0 1 1-1zm3 3v2h10v-2z"/></svg>
        </div>
        <div class="contact-line"><span>482 W 17th Avenue 9th Floor</span></div>
        <div class="contact-line"><span>New York, NY 10384</span></div>
      </address>
      <div class="header-rule"></div>
    </header>

    <section class="letter-body">
      <p class="salutation">Dear Mr Hale,</p>
      <p class="paragraph">Lorem ipsum dolor sit amet, consectetuer adipiscing elit, sed diam nonummy nibh euismod tincidunt ut laoreet dolore magna aliquam erat volutpat. Ut wisi enim ad minim veniam, quis nostrud exerci tation ullamcorper suscipit lobortis nisl ut aliquip ex ea commodo consequat. Duis autem vel eum iriure dolor in hendrerit in vulputate velit esse molestie consequat, vel illum dolore eu feugiat nulla facilisis at vero eros et accumsan et iusto odio dignissim qui blandit prae</p>
      <p class="paragraph">Lorem ipsum dolor sit amet, consectetuer adipiscing elit, sed diam nonummy nibh euismod tincidunt ut laoreet dolore magna aliquam erat volutpat. Ut wisi enim ad minim veniam, quis nostrud exerci tation ullamcorper suscipit lobortis nisl ut aliquip ex ea commodo consequat. Duis autem vel eum iriure dolor in hendrerit in vulputate velit esse molestie consequat, vel illum dolore eu feugiat nulla facilisis at vero eros et accumsan et iusto odio dignissim qui blandit prae</p>
      <p class="paragraph">Lorem ipsum dolor sit amet, consectetuer adipiscing elit, sed diam nonummy nibh euismod tincidunt ut laoreet dolore magna aliquam erat volutpat. Ut wisi enim ad minim veniam, quis nostrud exerci tation ullamcorper suscipit lobortis nisl ut aliquip ex ea com-</p>
      <p class="paragraph">Lorem ipsum dolor sit amet, consectetuer adipiscing elit, sed diam nonummy nibh euismod tincidunt ut laoreet dolore magna aliquam erat volutpat. Ut wisi enim ad minim veniam, quis nostrud exerci tation ullamcorper suscipit lobortis nisl ut aliquip ex ea com-</p>
      <p class="closing">Regards</p>
      <div class="signature" role="img" aria-label="Handwritten signature of the sender"></div>
    </section>

    <footer class="footer-band"></footer>
  </main>
</body>
</html>
```